Business card design needed

The company name is Pellwick Architects. We are an architectural company based in Melbourne,Australia that has a mix of client base from health care, commercial office, aged care, multi-residential, single residential and retail. Design type is contemporary.

Suggest the base colours need to be black and white. Please leave an area on the back of the card available for handwritten notes.

Target Market(s)

Generally corporate, aged 30 to 65

Industry/Entity Type

Residential

Contact Information for Business Card

Pellwick Architects
Dane Pellwick
7 Horbury Street
Northvale VIC 3059
T (03) 9572 4016
M 0431 607 295
E dp@pellwickarc.com.au

Logo Text

PA

Logo styles of interest
Emblem Logo
Abstract Logo
Lettermark Logo
Requirements
Must have
• I am having trouble attaching a sketch so would really appreciate your effort to try the following brief.

Black and White (B&W)
Would like different card cutout profile. Logo Example, use the half circle curve of the G to form the left edge of the card with no margin. The A is to sit inside the G, connected to the G by its horizontal. The A has its cross bar and lower right leg removed. Card in black, text in white.

Back of card to be black text on white background with services provided.

Client Focused Service
Architecture and Design
Functional Planning
Town Planning
Feasability Studies
Contract Documentation
Contract Administration
Project Management

Simple elegant text, Ariel or similar
Nice to have
• Integrated logo and card cut-out.

Card base black on front, white on back
Should not have
• Too many colours
Fussy details

```html
<!DOCTYPE html>
<html lang="en">
<head>
<meta charset="utf-8">
<title>Pellwick Architects – Business Card</title>
<link rel="stylesheet" href="https://fonts.googleapis.com/css2?family=Josefin+Sans:wght@400&display=swap">
<style>
  :root {
    --backdrop: #e9e6e1;
    --card-black: #0b0b0b;
    --card-edge: #161616;
    --wordmark: #2c2c2c;
    --text-light: #f2f2f2;
    --text-soft: #d6d6d6;
    --glow: rgba(255, 255, 255, 0.16);
  }
  * { margin: 0; padding: 0; box-sizing: border-box; }
  html, body {
    width: 1200px;
    height: 1000px;
    overflow: hidden;
    background: var(--backdrop);
  }
  .canvas {
    position: relative;
    width: 1200px;
    height: 1000px;
  }
  .card-front {
    position: absolute;
    left: 350px;
    top: 60px;
    width: 500px;
    height: 880px;
    background: var(--card-black);
    border: 1px solid var(--card-edge);
    box-shadow: 0 10px 30px rgba(0, 0, 0, 0.25);
    overflow: hidden;
    font-family: "Josefin Sans", Arial, sans-serif;
  }
  .wordmark {
    position: absolute;
    left: 0;
    right: 0;
    top: 190px;
    text-align: center;
    font-size: 40px;
    font-weight: 400;
    letter-spacing: 1px;
    color: var(--wordmark);
  }
  .contact-glow {
    position: absolute;
    left: 50%;
    top: 560px;
    width: 460px;
    height: 340px;
    transform: translateX(-50%);
    background: radial-gradient(ellipse at center, var(--glow) 0%, rgba(255,255,255,0.05) 45%, rgba(255,255,255,0) 70%);
  }
  .contact {
    position: absolute;
    left: 0;
    right: 0;
    top: 650px;
    text-align: center;
    color: var(--text-soft);
  }
  .contact-name {
    font-size: 32px;
    color: var(--text-light);
    letter-spacing: 0.5px;
    margin-bottom: 10px;
  }
  .contact-line {
    font-size: 16px;
    letter-spacing: 0.6px;
    line-height: 31px;
  }
</style>
</head>
<body>
  <main class="canvas">
    <section class="card-front">
      <div class="wordmark">Pellwick Architects</div>
      <div class="contact-glow"></div>
      <address class="contact" style="font-style: normal;">
        <p class="contact-name">Dane Pellwick</p>
        <p class="contact-line">7 Horbury Street Northvale VIC 3059</p>
        <p class="contact-line">T: (03) 9572 4016</p>
        <p class="contact-line">M: 0431 607 295</p>
        <p class="contact-line">E: dp@pellwickarc.com.au</p>
      </address>
    </section>
  </main>
</body>
</html>
```